Harbor Print Studio gallery website

I need a Website for a gallery with a shopify integration or maybe even better also compatible with squarespace.
the website should have following riders: Künstler, Veranstaltungen, Shop, About Us.
some nice examples for inspiration of the website architecture are:
https://www.tarnelgalerie.com/
https://www.mossline-gallery.com/de/
https://zinnbergalerie.de/
It should be easy for us to make adaptations and fill the website with new content.
Attached there is the CI an logo for the brand.
Art Collectors,
artgallery
3 page

```html
<!DOCTYPE html>
<html lang="en">
<head>
<meta charset="utf-8">
<title>Harbor Print Studio</title>
<link rel="stylesheet" href="https://fonts.googleapis.com/css2?family=Montserrat:wght@300;400;500&family=Open+Sans:wght@600;700;800&display=swap">
<style>
:root{
  --red:#c4161c;
  --ink:#1a1a1a;
  --muted:#555;
  --line:#d6d6d6;
  --white:#fff;
  --footer:#222;
  --icon-line:#bbb;
}
*{box-sizing:border-box;margin:0;padding:0}
html,body{width:1200px;height:3716px;overflow:hidden}
body{position:relative;background:var(--white);font-family:"Montserrat",sans-serif;color:var(--ink)}
.abs{position:absolute}

/* hero */
.hero{left:0;top:0;width:1200px;height:514px;
  background:linear-gradient(180deg,rgba(15,15,25,.55) 0%,rgba(0,0,0,.05) 40%,rgba(0,0,0,.5) 100%),
  linear-gradient(100deg,#2b2a3a 0%,#4a5670 25%,#7e2a30 45%,#5b6478 62%,#2d3142 85%,#1e2230 100%)}
.menu-icon{left:111px;top:58px}
.brand{left:0;width:1200px;top:74px;text-align:center;color:var(--white);font-weight:400;font-size:17px;letter-spacing:.3px;white-space:nowrap}
.brand .mark{display:inline-block;width:11px;height:11px;border:1.5px solid var(--white);margin-right:9px;vertical-align:0}
.hero-icons{left:1020px;top:54px;display:flex;gap:18px}
.hero-kicker{left:111px;top:351px;color:var(--white);font-family:"Open Sans",sans-serif;font-weight:800;font-size:27px;white-space:nowrap}
.hero-title{left:111px;top:385px;color:var(--white);font-family:"Open Sans",sans-serif;font-weight:800;font-size:42px;letter-spacing:.3px;white-space:nowrap}
.hero-arrows{left:111px;top:452px}
.btn{background:var(--red);color:var(--white);font-family:"Open Sans",sans-serif;font-weight:700;font-size:17px;display:flex;align-items:center;justify-content:center;white-space:nowrap}
.hero-btn{left:952px;top:379px;width:136px;height:45px}

/* section headings */
.section-title{left:0;width:1200px;text-align:center;font-weight:400;font-size:31px;letter-spacing:.5px;color:var(--ink);white-space:nowrap}

/* events */
.event{left:111px;width:977px;height:386px;color:var(--white);text-align:center}
.event-jazz{top:707px;background:linear-gradient(90deg,#3a2a22 0%,#7a5a3a 30%,#a8503a 50%,#6a4a33 70%,#2a2420 100%)}
.event-hall{top:1127px;background:radial-gradient(ellipse at 50% 40%,#6a5e4c 0%,#3e3a35 45%,#1f1f22 100%)}
.event::after{content:"";position:absolute;inset:0;background:rgba(0,0,0,.25)}
.event-body{position:relative;z-index:1;padding-top:128px}
.event-date{font-size:17px}
.event-name{font-size:40px;font-weight:400;margin-top:16px;white-space:nowrap}
.event-text{font-size:15px;margin-top:10px}

/* products */
.product{width:212px;text-align:center}
.product .art{width:212px;height:212px}
.product.active .art{outline:3px solid var(--red);outline-offset:-3px}
.product h3{font-family:"Open Sans",sans-serif;font-weight:700;font-size:19px;margin-top:26px;white-space:nowrap}
.product p{font-size:15px;color:#333;margin-top:5px;white-space:nowrap}
.product .price{font-size:16px;margin-top:16px;color:#222}

/* pagination */
.pager{left:455px;top:2970px;display:flex;gap:11px}
.pager span{width:32px;height:32px;border:1px solid var(--line);display:flex;align-items:center;justify-content:center;font-size:16px;color:#333}
.pager span.current{background:var(--red);border-color:var(--red);color:var(--white)}

/* newsletter */
.news-text{left:230px;width:740px;top:3218px;text-align:center;font-size:15.5px;line-height:29px;color:#444}
.email{left:310px;top:3335px;width:434px;height:47px;border:1px solid var(--line);font-size:15px;color:#999;padding-left:24px;display:flex;align-items:center}
.news-btn{left:754px;top:3335px;width:137px;height:47px}

/* footer */
.footer{left:0;top:3480px;width:1200px;height:236px;background:var(--footer);color:var(--white)}
.footer-brand{left:70px;top:138px;width:290px;text-align:center;font-size:21px;font-weight:400;white-space:nowrap}
.footer-brand .mark{display:inline-block;width:12px;height:12px;border:1.5px solid var(--white);margin-right:9px;vertical-align:1px}
.socials{left:584px;top:56px;display:flex;gap:18px}
.socials span{width:28px;height:28px;border:1.5px solid var(--icon-line)}
.footer-nav{left:581px;top:113px;display:flex;gap:32px;font-size:16px;white-space:nowrap}
.copyright{left:581px;top:157px;font-size:14px;color:#ddd;white-space:nowrap}
</style>
</head>
<body>

<header class="abs hero" role="img" aria-label="Painting of a rainy city street at night with cars and a figure holding a red umbrella"></header>
<svg class="abs menu-icon" width="22" height="16" viewBox="0 0 22 16" aria-hidden="true"><g stroke="#fff" stroke-width="2"><path d="M0 1h22M0 8h22M0 15h22"/></g></svg>
<div class="abs brand"><span class="mark"></span>HARBOR PRINT STUDIO</div>
<div class="abs hero-icons" aria-hidden="true">
  <svg width="26" height="24" viewBox="0 0 26 24"><path d="M13 22 3 12a5.5 5.5 0 0 1 10-7 5.5 5.5 0 0 1 10 7Z" fill="none" stroke="#fff" stroke-width="2"/></svg>
  <svg width="26" height="26" viewBox="0 0 26 26"><circle cx="11" cy="11" r="8.5" fill="none" stroke="#fff" stroke-width="2"/><path d="m17 17 7 7" stroke="#fff" stroke-width="2"/></svg>
</div>
<div class="abs hero-kicker">WELCOME TO</div>
<h1 class="abs hero-title">HARBOR PRINT STUDIO</h1>
<svg class="abs hero-arrows" width="80" height="24" viewBox="0 0 80 24" aria-hidden="true"><g fill="none" stroke-width="2"><path d="M26 12H2m9-9-9 9 9 9" stroke="#fff"/><path d="M44 12h24m-9-9 9 9-9 9" stroke="rgba(255,255,255,.45)"/></g></svg>
<a class="abs btn hero-btn">Explore</a>

<h2 class="abs section-title" style="top:595px">UPCOMING EVENTS</h2>

<article class="abs event event-jazz" role="img" aria-label="Painting of jazz musicians with trumpet and double bass">
  <div class="event-body"><div class="event-date">24/02/2024 - 25/02/2024</div><div class="event-name">Nostrud Exercitation</div><div class="event-text">Excepteur sint occaecat cupidatat non proident</div></div>
</article>
<article class="abs event event-hall" role="img" aria-label="Gallery hall with framed paintings and a visitor seen from behind">
  <div class="event-body"><div class="event-date">24/02/2024 - 25/02/2024</div><div class="event-name">Nostrud Exercitation</div><div class="event-text">Excepteur sint occaecat cupidatat non proident</div></div>
</article>

<h2 class="abs section-title" style="top:1632px">BUY FINE ARTS ONLINE</h2>

<div class="abs product" style="left:111px;top:1780px"><div class="art" role="img" aria-label="Colourful portrait painting with head wrap" style="background:linear-gradient(135deg,#2a6a8a,#6a3a1e 50%,#d08a2a)"></div><h3>LOREM IPSUM</h3><p>Lorem Ipsum sit amit</p><div class="price">$150</div></div>
<div class="abs product active" style="left:366px;top:1780px"><div class="art" role="img" aria-label="Botanical illustration with white lilies and figure" style="background:linear-gradient(160deg,#b8d4d2,#e9e0d4 50%,#d9734a)"></div><h3>LOREM IPSUM</h3><p>Lorem Ipsum sit amit</p><div class="price">$150</div></div>
<div class="abs product" style="left:622px;top:1780px"><div class="art" role="img" aria-label="Swirling sunset landscape with pine trees" style="background:linear-gradient(180deg,#f0a020,#e0442a 45%,#1f5a8a 80%,#14202a)"></div><h3>LOREM IPSUM</h3><p>Lorem Ipsum sit amit</p><div class="price">$150</div></div>
<div class="abs product" style="left:877px;top:1780px"><div class="art" role="img" aria-label="Abstract painting in blue, white and red" style="background:linear-gradient(135deg,#6fa8c8,#1e3a5a 45%,#e8e4e0 60%,#c01e24)"></div><h3>LOREM IPSUM</h3><p>Lorem Ipsum sit amit</p><div class="price">$150</div></div>

<div class="abs product" style="left:111px;top:2165px"><div class="art" role="img" aria-label="Grey sculpture made of broken fragments" style="background:linear-gradient(135deg,#8a8a8a,#3a3a3a 60%,#555)"></div><h3>LOREM IPSUM</h3><p>Lorem Ipsum sit amit</p><div class="price">$150</div></div>
<div class="abs product" style="left:366px;top:2165px"><div class="art" role="img" aria-label="Abstract red and gold flowing shapes" style="background:linear-gradient(135deg,#e8401a,#a8100e 50%,#f2b01e)"></div><h3>LOREM IPSUM</h3><p>Lorem Ipsum sit amit</p><div class="price">$150</div></div>
<div class="abs product" style="left:622px;top:2165px"><div class="art" role="img" aria-label="Close-up painted portrait in soft pastel tones" style="background:linear-gradient(180deg,#efe2dc,#d8a8a0 60%,#c8524a)"></div><h3>LOREM IPSUM</h3><p>Lorem Ipsum sit amit</p><div class="price">$150</div></div>
<div class="abs product" style="left:877px;top:2165px"><div class="art" role="img" aria-label="Vivid multicoloured portrait painting" style="background:linear-gradient(135deg,#1e4a8a,#e0782a 45%,#c8245a 75%,#2a1e4a)"></div><h3>LOREM IPSUM</h3><p>Lorem Ipsum sit amit</p><div class="price">$150</div></div>

<div class="abs product" style="left:111px;top:2560px"><div class="art" role="img" aria-label="Torn paper collage in coral and white" style="background:linear-gradient(135deg,#e88a7a,#f0ece6 50%,#d8c8b8)"></div><h3>LOREM IPSUM</h3><p>Lorem Ipsum sit amit</p><div class="price">$150</div></div>
<div class="abs product" style="left:366px;top:2560px"><div class="art" role="img" aria-label="Yellow watercolour abstract" style="background:radial-gradient(circle at 40% 60%,#e8a41e,#f4d45a 55%,#f6ecc8)"></div><h3>LOREM IPSUM</h3><p>Lorem Ipsum sit amit</p><div class="price">$150</div></div>
<div class="abs product" style="left:622px;top:2560px"><div class="art" role="img" aria-label="Pop art portrait with flowers in pink and teal" style="background:linear-gradient(135deg,#e07aa0,#3aa8a8 50%,#f0c040)"></div><h3>LOREM IPSUM</h3><p>Lorem Ipsum sit amit</p><div class="price">$150</div></div>
<div class="abs product" style="left:877px;top:2560px"><div class="art" role="img" aria-label="Painted group of people in profile" style="background:linear-gradient(90deg,#c8c0b0,#5a4030 50%,#a8a090)"></div><h3>LOREM IPSUM</h3><p>Lorem Ipsum sit amit</p><div class="price">$150</div></div>

<nav class="abs pager">
  <span>&#9664;</span><span class="current">1</span><span>2</span><span>&hellip;</span><span>9</span><span>10</span><span>&#9654;</span>
</nav>

<h2 class="abs section-title" style="top:3132px">SIGNUP FOR NEWSLETTER</h2>
<p class="abs news-text">Lorem ipsum dolor sit amet, consectetur adipiscing elit, sed do eiusmod tempor incididunt ut labore et dolore magna aliqua. Quis ipsum suspendisse ultrices gravida.</p>
<div class="abs email">Email ID</div>
<a class="abs btn news-btn">Explore</a>

<footer class="abs footer">
  <div class="abs footer-brand"><span class="mark"></span>HARBOR PRINT STUDIO</div>
  <div class="abs socials"><span aria-label="Social link 1"></span><span aria-label="Social link 2"></span><span aria-label="Social link 3"></span><span aria-label="Social link 4"></span></div>
  <nav class="abs footer-nav"><span>Home</span><span>Artists</span><span>Events</span><span>Shop</span><span>About Us</span><span>Contact Us</span></nav>
  <div class="abs copyright">2024 Harbor Print Studio. All Rights Reserved.</div>
</footer>

</body>
</html>
```